Business Card Design

I do estate sales and would like business card to reflect look and feel of attached logo. I also have copy of logo in .eps and .tif if you need that instead of .jpeg.
Updates

sorry for the delay in reviewing these designs. I will pick one by tomorrow. Here are the absolutes: *must have tagline (we find good homes for your treasures *must use blue and green *must be horizontal *nothing too fancy please submit your best and final. Thanks so much!

Industry/Entity Type

Business

Contact Information for Business Card

Mira Tolland

TAGS by MIRA
We find good homes for your treasures.

Specializing in one to three-day sales
o (no sale too big or too small)
• Home and garage organizing
• Home Clean-out

Call Mira Tolland at 202-555-0147
to schedule.

```html
<!DOCTYPE html>
<html lang="en">
<head>
<meta charset="utf-8">
<title>Mira Tolland – Tags by Mira Business Card</title>
<link href="https://fonts.googleapis.com/css2?family=Cabin:ital,wght@0,600;0,700;1,400;1,700&display=swap" rel="stylesheet">
<style>
  :root {
    --teal: #137fa0;
    --green: #6b7f3a;
    --paper: #ffffff;
  }
  * { margin: 0; padding: 0; box-sizing: border-box; }
  html, body { width: 1200px; height: 704px; overflow: hidden; background: var(--paper); }
  .card {
    position: relative;
    width: 1200px;
    height: 704px;
    background: var(--paper);
    font-family: "Cabin", "Gill Sans", sans-serif;
    overflow: hidden;
  }
  .side-band {
    position: absolute;
    left: 0; top: 0;
    width: 272px; height: 704px;
    background: var(--teal);
  }
  .owner-name {
    position: absolute;
    left: 309px; top: 168px;
    font-weight: 700;
    font-size: 46px;
    letter-spacing: 1px;
    color: var(--teal);
    line-height: 1;
  }
  .brand-frame {
    position: absolute;
    left: 735px; top: -1px;
    width: 466px; height: 382px;
    border-left: 1.5px solid var(--teal);
    border-bottom: 1.5px solid var(--teal);
    display: flex;
    align-items: center;
    justify-content: center;
  }
  .brand-name {
    font-weight: 600;
    font-size: 64px;
    color: var(--green);
    letter-spacing: 2px;
  }
  .details {
    position: absolute;
    left: 272px; width: 928px;
    text-align: center;
    color: var(--green);
    font-style: italic;
  }
  .tagline { top: 442px; font-weight: 700; font-size: 28px; }
  .services { top: 509px; font-weight: 400; font-size: 19.5px; }
  .size-note { top: 551px; font-weight: 400; font-size: 19.5px; }
  .call-to-action { top: 619px; font-weight: 700; font-size: 34px; }
</style>
</head>
<body>
  <div class="card">
    <div class="side-band"></div>

    <h1 class="owner-name">MIRA TOLLAND</h1>

    <div class="brand-frame">
      <span class="brand-name">TAGS by MIRA</span>
    </div>

    <p class="details tagline">We find good homes for your treasures</p>
    <p class="details services">Specializing in one to three-day sales • Home and garage organizing • Home clean-out</p>
    <p class="details size-note">(no sale too big or too small)</p>
    <p class="details call-to-action">Call Mira Tolland at 202-555-0147 to schedule</p>
  </div>
</body>
</html>
```